Bright, Fun and hard to forget home inspection business card.

We need a Business card design for a new Home Inspection company. We are building a brand that is bright, fun and easy to remember.

Target Market(s)

Anyone involed in buying and selling of homes.

Industry/Entity Type

Home Inspection

Contact Information for Business Card

Colin Marlowe Owner/Inspector

Wedsite- PorchAndRafterCheck.example
Phone: 253-555-0187
Email- ColinMarlowe@mailbox.example
WA Lic # 4806

Requirements
Must have
• BRQV LOGO somewhere on card.

```html
<!DOCTYPE html>
<html lang="en">
<head>
<meta charset="utf-8">
<title>Porch And Rafter Check – Business Card</title>
<link rel="stylesheet" href="https://fonts.googleapis.com/css2?family=Open+Sans:wght@400;600;700;800&display=swap">
<style>
  :root {
    --stage: #2b2b2b;
    --orange: #e2552b;
    --orange-deep: #d2461f;
    --orange-soft: #ea7a52;
    --ink: #1b1b1b;
    --paper: #f7f7f7;
    --white: #ffffff;
    --muted: #f3d2c4;
    --card-w: 340px;
    --card-h: 595px;
  }
  * { box-sizing: border-box; margin: 0; padding: 0; }
  html, body {
    width: 1200px; height: 873px; overflow: hidden;
    background: var(--stage);
    font-family: "Open Sans", Arial, sans-serif;
  }
  .stage {
    width: 1200px; height: 873px;
    display: flex; justify-content: center; align-items: center; gap: 80px;
  }
  .card {
    position: relative;
    width: var(--card-w); height: var(--card-h);
    border-radius: 22px; overflow: hidden;
  }

  /* Back side */
  .card--back {
    background: linear-gradient(160deg, var(--orange-soft) 0%, var(--orange) 45%, var(--orange-deep) 100%);
  }
  .tagline { position: absolute; left: 34px; top: 70px; }
  .tagline__lead { color: var(--muted); font-weight: 700; font-size: 17px; }
  .tagline__big { color: var(--ink); font-weight: 800; font-size: 38px; line-height: 1.05; letter-spacing: -0.5px; }
  .tagline__row { display: flex; align-items: center; gap: 10px; margin-top: 4px; }
  .tagline__amp { color: var(--white); font-size: 72px; font-weight: 400; font-family: Georgia, serif; line-height: 1; }
  .tagline__easy { color: var(--ink); font-weight: 800; font-size: 25px; line-height: 1.05; }

  .brand { position: absolute; left: 0; right: 0; display: flex; align-items: center; justify-content: center; gap: 10px; }
  .brand__figure { width: 110px; height: 130px; border-radius: 14px; }
  .brand__name { font-weight: 800; font-size: 26px; line-height: 1.0; text-transform: uppercase; }
  .card--back .brand { top: 330px; }
  .card--back .brand__figure { background: linear-gradient(180deg, #f4f4f4, #cfcfcf); }
  .card--back .brand__name { color: var(--white); }

  /* Front side */
  .card--front { background: var(--paper); }
  .person { position: absolute; top: 34px; left: 0; right: 0; text-align: center; }
  .person__name { font-weight: 800; font-size: 22px; color: var(--ink); }
  .person__role { font-size: 15px; color: var(--ink); margin-top: 2px; }
  .card--front .brand { top: 110px; }
  .card--front .brand__figure { background: linear-gradient(180deg, var(--orange-soft), var(--orange)); }
  .card--front .brand__name { color: var(--orange); }

  .license { position: absolute; top: 262px; right: 30px; display: flex; align-items: center; gap: 10px; font-size: 15px; color: var(--ink); }
  .license__badge { width: 42px; height: 42px; background: var(--ink); border-radius: 4px; }

  .skyline { position: absolute; left: 0; right: 0; top: 318px; height: 62px; background: linear-gradient(180deg, var(--paper), var(--orange)); }
  .band { position: absolute; left: 0; right: 0; top: 380px; bottom: 0; background: var(--orange); }
  .contacts { list-style: none; position: absolute; left: 24px; top: 415px; right: 14px; }
  .contacts li { display: flex; align-items: center; gap: 14px; color: var(--white); font-size: 14px; height: 46px; }
  .contacts svg { width: 26px; height: 26px; flex: none; }
</style>
</head>
<body>
<main class="stage">

  <section class="card card--back" aria-label="Card back">
    <div class="tagline">
      <p class="tagline__lead">Brand that is...</p>
      <p class="tagline__big">BRIGHT, FUN</p>
      <div class="tagline__row">
        <span class="tagline__amp">&amp;</span>
        <span class="tagline__easy">Easy<br>to Remember</span>
      </div>
    </div>
    <div class="brand">
      <div class="brand__figure" role="img" aria-label="Cartoon inspector with a megaphone"></div>
      <p class="brand__name">Porch And<br>Rafter<br>Check</p>
    </div>
  </section>

  <section class="card card--front" aria-label="Card front">
    <div class="person">
      <p class="person__name">Colin Marlowe</p>
      <p class="person__role">Owner/Inspector</p>
    </div>
    <div class="brand">
      <div class="brand__figure" role="img" aria-label="Cartoon inspector with a megaphone"></div>
      <p class="brand__name">Porch And<br>Rafter<br>Check LLC</p>
    </div>
    <div class="license">
      <span>WA Lic # 4806</span>
      <span class="license__badge" aria-label="Certification badge"></span>
    </div>
    <div class="skyline" role="img" aria-label="City skyline silhouette"></div>
    <div class="band"></div>
    <ul class="contacts">
      <li>
        <svg viewBox="0 0 24 24" fill="none" stroke="#fff" stroke-width="1.8"><path d="M3 9c0-3 4-5 9-5s9 2 9 5l-3 1-2-3H8L6 10z"/><rect x="6" y="12" width="12" height="8" rx="1.5"/></svg>
        <span>253-555-0187</span>
      </li>
      <li>
        <svg viewBox="0 0 24 24" fill="none" stroke="#fff" stroke-width="1.8"><rect x="3" y="6" width="18" height="12" rx="1"/><path d="M3 6l9 7 9-7"/></svg>
        <span>ColinMarlowe@mailbox.example</span>
      </li>
      <li>
        <svg viewBox="0 0 24 24" fill="none" stroke="#fff" stroke-width="1.8"><circle cx="12" cy="12" r="9"/><path d="M3 12h18M12 3c3 3 3 15 0 18M12 3c-3 3-3 15 0 18"/></svg>
        <span>www.PorchAndRafterCheck.example</span>
      </li>
    </ul>
  </section>

</main>
</body>
</html>
```